Brochure for Dog Daycare/Overnight Facility

Looking for a multi page brochure for my dog daycare, overnight care, and grooming facility.

Content to be taken from our current website. Please note our website will be updated so please don't take any design elements from it.

Brochure should be professional yet personable with stock images of dogs playing and having fun.

Please see the attached file with the business card so you can see the blue and green colors that we use to brand ourselves.

Here are the different sections to include for content which can all be found on our website at: www.PawHavenLodge.com

Highlight our three main services: Go to the services tab and pull the content from Daycare, Overnight Care, and Grooming.

Use testimonials throughout found: About us tab, left side of page under 'what our clients say'.

Facility highlights: About us tab, left side under 'Facility'.

What makes us different: About us tab, left side of page.

Include the following Frequently Asked Questions and answers:
What is dog daycare?
How often do dog owners take their dogs to Daycare?
I have an old dog, will he/she enjoy this environment?
Does my dog have to be spayed or neutered?
Do you offer indoor and outdoor play areas?
Can I take a tour?
What qualifications do staff members have?
What sets you apart from your competitors?

Make sure to include: phone number, web address, e-mail address, mailing address.
Updates

Thank you all for your submissions.  We are having a hard time deciding with this project.  Hope to have made a decision in the next day or so.

Target Market(s)

Dog owners would love their pets. Medium to higher income. Ages 25-60.

Industry/Entity Type

Business

Requirements
Must have
• Must have all of the content pulled from our website.

Photos of dogs and dogs playing.

Our contact information.

Nice to have
• I would like a corresponding price sheet that is not part of the brochure but can be slid inside. Our pricing can be found on our website. I can get into more specifics on pricing if you choose to provide this option.
Should not have
• Anything cat related.

Should not be cutesie, must be professional and personable. Displaying trust.

```html
<!DOCTYPE html>
<html lang="en">
<head>
<meta charset="utf-8">
<title>Paw Haven Lodge – Brochure and Price Sheet</title>
<link rel="stylesheet" href="https://fonts.googleapis.com/css2?family=Questrial&family=Varela+Round&display=swap">
<style>
:root{
  --bg:#111;
  --sky:#a9dbe1;
  --sky-deep:#7fc3cc;
  --lime:#a4c23a;
  --lime-deep:#8aab22;
  --lime-pale:#e1ebbd;
  --brown:#4b3a2c;
  --ink:#333;
  --muted:#666;
  --paper:#fff;
}
*{box-sizing:border-box;margin:0;padding:0}
html,body{width:1200px;height:1000px;overflow:hidden;background:var(--bg)}
body{position:relative;font-family:"Questrial",Arial,sans-serif;color:var(--ink)}

.spread{position:absolute;width:448px;height:470px;display:flex;box-shadow:0 4px 16px rgba(0,0,0,.5)}
.sheet{position:absolute;width:224px;height:470px;box-shadow:0 4px 16px rgba(0,0,0,.5)}
.page{position:relative;width:224px;height:470px;background:var(--paper);overflow:hidden;font-size:6.2px;line-height:1.4;display:flex;flex-direction:column}
.spread .page:first-child{box-shadow:inset -6px 0 8px -6px rgba(0,0,0,.25)}

.band{height:52px;background:var(--sky);position:relative;flex:none}
.stripe{height:7px;background:var(--lime);flex:none}
.brand{display:flex;align-items:center;gap:5px;color:var(--brown);font-family:"Questrial",Arial,sans-serif;letter-spacing:.08em;text-transform:uppercase}
.brand-mark{width:12px;height:12px;background:var(--brown);flex:none}
.band .brand{position:absolute;left:12px;bottom:6px;font-size:9px;background:var(--paper);padding:4px 6px}
.contact-line{font-size:5.2px;color:var(--lime-deep);padding:2px 12px}
.band-title{position:absolute;left:0;right:0;bottom:-12px;text-align:center;font-family:"Varela Round",Arial,sans-serif;font-size:13px;color:var(--lime-deep);font-weight:400}
.band-title.on-stripe{bottom:-17px}

.body{padding:10px 12px;flex:1;display:flex;flex-direction:column;gap:5px}
h3{font-family:"Varela Round",Arial,sans-serif;font-size:7.4px;color:var(--ink);font-weight:400;text-align:center}
h4{font-family:"Varela Round",Arial,sans-serif;font-size:6.6px;color:var(--ink);font-weight:400}
p{color:var(--muted)}
.lead{font-style:italic;color:var(--ink)}

.photo{flex:none;border-radius:1px}
.photo-grass{background:linear-gradient(160deg,#9cbf59 0%,#6f9a34 55%,#4f7a22 100%)}
.photo-dogs-white{background:linear-gradient(180deg,#fdfdfd 0%,#e6e3de 60%,#c9c4bc 100%)}
.photo-building{background:linear-gradient(180deg,#2e6fd1 0%,#4b86d8 40%,#a8a39b 62%,#5d6b4a 100%)}
.photo-group{background:linear-gradient(180deg,#ffffff 0%,#efe9e2 45%,#b99c82 75%,#6a5645 100%)}

.panel{background:var(--lime-pale);padding:7px 10px;border-radius:0 14px 0 0}
.panel h4{color:var(--lime-deep);margin-bottom:3px}
.ticks{list-style:none;display:flex;flex-direction:column;gap:3px}
.ticks li{display:flex;gap:4px;align-items:flex-start;color:var(--muted)}
.ticks svg{flex:none;width:6px;height:6px;margin-top:1px}

/* cover */
.cover-back{background:var(--lime)}
.cover-back .photo{height:250px}
.cover-back .info{padding:16px 16px;color:var(--brown);font-size:8px;line-height:1.5}
.cover-back .web{font-size:11px;letter-spacing:.04em;margin-bottom:8px}
.cover-back .hours{margin-top:8px;text-transform:uppercase}
.cover-front .photo{height:200px}
.cover-front .welcome{background:var(--lime);flex:1;padding:10px 14px;color:var(--brown);font-size:6.4px;display:flex;flex-direction:column;gap:6px}
.welcome h2{font-family:"Varela Round",Arial,sans-serif;font-weight:400;font-size:9px;text-align:center;text-transform:uppercase;color:#fff;background:var(--sky-deep);margin:0 -14px;padding:3px 0}
.welcome .tagline{text-align:center;font-size:7px}
.welcome .cols{display:flex;justify-content:space-between}
.welcome .phone{text-align:center;font-size:9px;margin-top:auto}

/* rates */
.rates h3{font-size:8px;margin-bottom:2px}
.rate-group{font-family:"Varela Round",Arial,sans-serif;font-size:6.6px;margin-top:4px}
table{border-collapse:collapse;width:100%;font-size:6px}
td{border:1px solid #bbb;padding:2px 4px;color:var(--ink)}
td:last-child{width:40%}

.quotes p{margin-bottom:1px}
.quotes .who{font-weight:700;color:var(--ink);margin-bottom:4px}
.quotes-title{position:absolute;left:60px;top:10px;font-family:"Varela Round",Arial,sans-serif;font-size:15px;line-height:1.05;color:#fff;text-align:center}
.faq h4{margin-top:2px;font-style:italic}
</style>
</head>
<body>

<!-- ===== Row 1: outer cover ===== -->
<section class="spread" style="left:20px;top:20px" aria-label="Brochure outside cover">
  <div class="page cover-back">
    <div class="band"><div class="brand"><span class="brand-mark"></span>Paw Haven Lodge</div></div>
    <div class="photo photo-building" role="img" aria-label="Photo of the lodge building under a blue sky"></div>
    <div class="info">
      <div class="web">WWW.PAWHAVENLODGE.COM</div>
      <div>480 Maple Grove Drive<br>Lakeview, WI 54000</div>
      <div style="margin-top:6px">P: 555.014.2772<br>F: 555.014.2773</div>
      <div class="hours">Monday – Friday 6-6<br>Saturday 8-6<br>Sunday 10-6</div>
    </div>
  </div>
  <div class="page cover-front">
    <div class="band"><div class="brand"><span class="brand-mark"></span>Paw Haven Lodge</div></div>
    <div class="photo photo-group" role="img" aria-label="Photo of a group of dogs sitting together"></div>
    <div class="welcome">
      <h2>Welcome to Paw Haven Lodge</h2>
      <p class="tagline" style="color:var(--brown)">Experience the most luxurious and enjoyable pet resort in Lake Country, dedicated to the health and happiness of your best friend.</p>
      <p class="tagline" style="color:var(--brown)">Paw Haven Lodge – The Next Best Thing to Being Home</p>
      <div class="cols">
        <div>Dog Daycare<br>Overnight Care<br>Grooming &amp; Spa Services</div>
        <div>Custom Activity Packages<br>All Natural Gourmet Treats<br>Grain Free Pet Food<br>Large Grass Play Yards</div>
      </div>
      <div class="phone">555.014.2772</div>
    </div>
  </div>
</section>

<!-- ===== Row 1: about / services ===== -->
<section class="spread" style="left:488px;top:20px" aria-label="About us and daycare spread">
  <div class="page">
    <div class="band"><div class="brand"><span class="brand-mark"></span>Paw Haven Lodge</div></div>
    <div class="stripe"></div>
    <div class="contact-line">555.014.2772 · info@pawhavenlodge.com</div>
    <div class="body">
      <h3>About Us</h3>
      <p class="lead">We have gone to great lengths to make sure that the environment that your dog stays in while at Paw Haven Lodge is safe, comfortable, and enjoyable.</p>
      <p>That starts with our facilities. We use an air purification system throughout to help eliminate the spread of dust, pollen and allergens. Clean air is the first step toward a healthy stay. Our indoor play yard and overnight suites use recycled rubber flooring that is easy on joints and paws.</p>
      <p>We also have a grass yard for outdoor play, so every guest can enjoy fresh air and sunshine. Our team watches every group closely and keeps each dog comfortable all day.</p>
      <div class="photo photo-grass" role="img" aria-label="Photo of two dogs running on grass" style="height:80px;margin:2px 0 2px 60px"></div>
      <div class="panel">
        <h4>What makes us different.</h4>
        <ul class="ticks">
          <li><svg viewBox="0 0 6 6"><circle cx="3" cy="3" r="3" fill="#a4c23a"/></svg>Our level of customer service and care</li>
          <li><svg viewBox="0 0 6 6"><circle cx="3" cy="3" r="3" fill="#a4c23a"/></svg>We treat your pet like a member of our family</li>
          <li><svg viewBox="0 0 6 6"><circle cx="3" cy="3" r="3" fill="#a4c23a"/></svg>An emphasis on continued staff training</li>
          <li><svg viewBox="0 0 6 6"><circle cx="3" cy="3" r="3" fill="#a4c23a"/></svg>Individualized attention, one person per twenty dogs</li>
          <li><svg viewBox="0 0 6 6"><circle cx="3" cy="3" r="3" fill="#a4c23a"/></svg>No cages or crates for the pet</li>
        </ul>
      </div>
    </div>
  </div>
  <div class="page">
    <div class="band"><div class="band-title">Our Services</div></div>
    <div class="stripe"></div>
    <div class="body" style="padding-top:16px">
      <p class="lead">At Paw Haven Lodge we take pride in offering a wide variety of services, packages, high-quality retail goods, and à la carte offerings.</p>
      <p>Our philosophy behind this is simple: every dog is unique. Not all dogs want to or are able to take part in daycare, so every guest is treated as an individual. Your dog may be the type that prefers a quiet day, or may need lots of play to burn off energy. We let the dog tell us what it needs.</p>
      <h3 style="margin-top:4px">Daycare</h3>
      <p>You work long hours and hate to leave your dog home alone all day. While staying at Paw Haven Lodge your dog will play and socialize in a safe and supervised environment with other dogs of the same size or temperament.</p>
      <p>Socialization is one of the most important aspects of canine development. Daycare is an excellent way for canines to learn their social skills as well as burn off excess energy.</p>
      <p>At Paw Haven Lodge dogs will have the chance to wrestle, play, and run around in large, safe yards. Our staff watches each group and every step is taken to deliver the utmost in social interaction, safety and fun. Dogs will take part in play groups determined by size and temperament.</p>
      <p>The benefits of dog daycare are numerous. Your dog's social skills will grow while learning how to play and interact with others in a relaxed and appropriate way. Boredom and destructive behaviors caused by lack of activity and separation anxiety will decrease.</p>
    </div>
  </div>
</section>

<!-- ===== Row 1: price sheet ===== -->
<section class="sheet" style="left:956px;top:20px" aria-label="Price sheet">
  <div class="page rates">
    <div class="band"><div class="brand"><span class="brand-mark"></span>Paw Haven Lodge</div></div>
    <div class="stripe"></div>
    <div class="contact-line">555.014.2772 · info@pawhavenlodge.com</div>
    <div class="body" style="gap:2px">
      <h3>Rates</h3>
      <div class="rate-group">Daycare Rates</div>
      <table>
        <tr><td>Half Day</td><td>$14.50</td></tr>
        <tr><td>5 Half Days</td><td>$70</td></tr>
        <tr><td>10 Half Days</td><td>$135</td></tr>
        <tr><td>&nbsp;</td><td></td></tr>
        <tr><td>Full Day</td><td>$19.50</td></tr>
        <tr><td>5 Full Days</td><td>$95</td></tr>
        <tr><td>10 Full Days</td><td>$185</td></tr>
        <tr><td>20 Full Days</td><td>$365</td></tr>
      </table>
      <div class="rate-group">Gourmet Treats</div>
      <table>
        <tr><td>Ice Cream Social</td><td>$1.50</td></tr>
        <tr><td>Marrow Bone</td><td>$3</td></tr>
        <tr><td>Seasonal Feast</td><td>$3.50</td></tr>
      </table>
      <div class="rate-group">Grooming and Spa Rates</div>
      <table>
        <tr><td>Nail Trim</td><td>$14</td></tr>
        <tr><td>Teeth Brushing</td><td>$4</td></tr>
        <tr><td>Ear Plucking</td><td>$10</td></tr>
        <tr><td>Flea &amp; Tick Treatment</td><td>$10</td></tr>
      </table>
      <div class="rate-group">Overnight Care</div>
      <p>Paw Haven Lodge offers a wide variety of activity and vacation options to suit the needs of every dog. Call today to talk to a reservation specialist.</p>
    </div>
  </div>
</section>

<!-- ===== Row 2: overnight / grooming ===== -->
<section class="spread" style="left:20px;top:510px" aria-label="Overnight care and grooming spread">
  <div class="page">
    <div class="band"><div class="brand"><span class="brand-mark"></span>Paw Haven Lodge</div></div>
    <div class="stripe"></div>
    <div class="contact-line">555.014.2772 · info@pawhavenlodge.com</div>
    <div class="body">
      <h3>Overnight Care</h3>
      <p class="lead">Leaving your pet overnight should not be a stressful time for either of you. Your pet's stay with us should be safe and enjoyable, just like being at home.</p>
      <p>Each guest will enjoy a peaceful night's sleep in a private suite and lots of time to rest. Custom suites with raised beds are available for those families with multiple pets.</p>
      <p>For the comfort of each guest the latest flooring and climate control systems are found throughout all indoor play and sleeping areas. And you'll be pleased to know we have attendants on call 24 hours a day.</p>
      <p>You know that the more activity and interaction you get involves, the happier and healthier they will be. Activity does not mean exercise; it could be extra cuddle time, feedings or a trip to the groomer to work on nail trimming or brushing. Either way it is important to provide your dog extra attention while away from home.</p>
      <div class="panel" style="margin:8px -12px 0;border-radius:0 14px 0 0">
        <h4>Why Activities?</h4>
        <ul class="ticks">
          <li><svg viewBox="0 0 6 6"><circle cx="3" cy="3" r="3" fill="#4b3a2c"/></svg>Exercise helps keep dogs agile and mobile</li>
          <li><svg viewBox="0 0 6 6"><circle cx="3" cy="3" r="3" fill="#4b3a2c"/></svg>Dogs need physical and mental stimulation daily to thrive</li>
          <li><svg viewBox="0 0 6 6"><circle cx="3" cy="3" r="3" fill="#4b3a2c"/></svg>Helps channel energy into more productive outlets</li>
          <li><svg viewBox="0 0 6 6"><circle cx="3" cy="3" r="3" fill="#4b3a2c"/></svg>Can help timid dogs build trust and confidence</li>
          <li><svg viewBox="0 0 6 6"><circle cx="3" cy="3" r="3" fill="#4b3a2c"/></svg>Exercise reduces digestive problems</li>
        </ul>
      </div>
    </div>
  </div>
  <div class="page">
    <div class="band"><div class="band-title on-stripe">Our Services</div></div>
    <div class="stripe"></div>
    <div class="body" style="padding-top:20px">
      <h3>Grooming</h3>
      <p class="lead">What better way to pamper your pooch than with a special treatment at our full service grooming spa. Every dog deserves the best, which is why our professional dog groomers are ready to cater to their every need. Our high quality full service grooming includes a bath with your choice of shampoo, nail trim, ear cleaning, brush out and haircut if necessary.</p>
      <p>Every grooming service uses all natural products so you can be sure your dog is only getting the best. From teeth cleaning to a quick spritz of detangler or a relaxing pawdicure, every treatment or service is also available à la carte and can be done on their own or as the perfect complement to any other grooming service.</p>
      <p>Prices for grooming services may vary by breed, size or coat condition and are performed by appointment only. Please call today to schedule or ask about any of our fabulous spa services.</p>
      <p>Proof of Rabies vaccination and a completed application packet is required prior to any grooming service.</p>
      <div class="photo photo-dogs-white" role="img" aria-label="Photo of two dogs playing together" style="height:110px;margin-top:auto"></div>
    </div>
  </div>
</section>

<!-- ===== Row 2: FAQ ===== -->
<section class="spread" style="left:488px;top:510px" aria-label="Frequently asked questions spread">
  <div class="page faq">
    <div class="band"><div class="brand"><span class="brand-mark"></span>Paw Haven Lodge</div></div>
    <div class="stripe"></div>
    <div class="contact-line">555.014.2772 · info@pawhavenlodge.com</div>
    <div class="body" style="gap:3px">
      <h3>FAQ</h3>
      <h4>What is dog daycare?</h4>
      <p>Dog daycare is a safe, fun, social play environment for your dog. It works a lot like human daycare in that you can drop your dog off for any number of hours during a day, and they will be able to play with other dogs, staff members, inside and outside all day.</p>
      <h4>How often do dog owners take their dogs to Daycare?</h4>
      <p>It varies greatly from client to client. We have some guests that visit daily and others that only visit a couple of times per month. The amount of daycare you feel is necessary for your dog to maintain a healthy and active lifestyle is a decision only you can make.</p>
      <h4>I have an old dog, will he/she enjoy this environment?</h4>
      <p>Dogs of every age and activity level have enjoyed all of our services. Our staff members cater to the individual needs of each guest every day to ensure a positive experience during every visit. Older dogs may not run around all day as much as the younger dogs, but they still enjoy being around other dogs.</p>
      <h4>Does my dog have to be spayed or neutered?</h4>
      <p>In order to take part in daycare or group play all dogs must be spayed or neutered before the age of 7 months. Unaltered pets are however welcome to take part in Overnight Care and Grooming Services.</p>
      <h4>Do you offer indoor and outdoor play areas?</h4>
      <p>You can facility offers indoor and outdoor play areas for both large and small dogs.</p>
      <h4>What qualifications do staff members have?</h4>
      <p>We have a team of very qualified individuals at each facility. Staff members are certified in Canine First Aid and CPR and are trained in dog behavior and group play monitoring.</p>
    </div>
  </div>
  <div class="page faq">
    <div class="band"><div class="band-title on-stripe">FAQ</div></div>
    <div class="stripe"></div>
    <div class="body" style="padding-top:20px;gap:3px">
      <h4>Can I take a tour?</h4>
      <p>Absolutely! Our client services staff members are more than happy to take you on an informative tour through the public areas of any Paw Haven Lodge location and share with you everything Paw Haven Lodge has to offer. Tours are welcome anytime during normal business hours.</p>
      <h4>What sets you apart from your competitors?</h4>
      <p>Paw Haven Lodge offers the widest variety of services and amenities dedicated to the health and happiness of each guest. We recognize that each guest has a different personality with different needs, which is why we come highly recommended by leading veterinary clinics throughout Lake Country.</p>
      <div class="photo photo-grass" role="img" aria-label="Photo of a golden puppy running across grass" style="height:150px;margin-top:14px"></div>
    </div>
  </div>
</section>

<!-- ===== Row 2: testimonials ===== -->
<section class="sheet" style="left:956px;top:510px" aria-label="Client testimonials">
  <div class="page quotes">
    <div class="band" style="height:60px"><div class="quotes-title">What our<br>clients say</div></div>
    <div class="stripe"></div>
    <div class="body" style="gap:0">
      <p>I would recommend Paw Haven Lodge to any and everyone who is looking for a daycare they can trust. Our pup is not just a pet, he is a part of my family and they treat him as part of theirs as well. This is a five-star facility for my pet and I just want to say thank you to all of the staff for being so loving and caring.</p>
      <p class="who">- Carla Voss &amp; Ben Ortiz, owners of Putz</p>
      <p>I was thrilled to find Paw Haven Lodge, a place for Miracle where she gets the same amount of love and attention that she gets when she's home.</p>
      <p class="who">-Dana, owner of Miracle</p>
      <p>We have had pets for the last 26 years and the quality of service provided by Paw Haven Lodge is among the best I have encountered. My family is confident when we are on vacation the dogs are also on their own vacation enjoying quality care.</p>
      <p class="who">-Marta</p>
      <p>Paw Haven Lodge is a wonderful facility with a dedicated and caring staff. We use the Lodge for training classes, daycare, overnight extended care and grooming. We've been very pleased with their services and the best part is Murphy loves going.</p>
      <p class="who">-Rob and Lisa Keene, owners of Murphy</p>
      <p>Hannah is part of our family. When we drop her off for daycare we know she is in good hands. After all, Paw Haven Lodge is all about the dogs!</p>
      <p class="who">-Tim and Ann Walsh, owners of Hannah</p>
      <p>Ricco is my baby and I wouldn't ask for better people to look after him during the day. I know that he is 100% safe and being taken care of like I would take care of him.</p>
      <p class="who">-Kay Lindgren, owner of Ricco</p>
      <p>I cannot feel more comfortable putting the thing I care about very much and relies on me to home a good life, with anyone besides the people at Paw Haven Lodge. Holly is exactly that.</p>
      <p class="who">-Jo Pearce, owner of Holly</p>
    </div>
  </div>
</section>

</body>
</html>
```